Stationary for Wealth Management Firm

We need stationary design based on our new business cards. We would like it to be simple, clean and understated. A lot of our clients are seniors so the fonts cannot be too small. Our colors are dark blue and light grey.

This is what we need:

1. Letterhead US Letter – 8.5" x 11" CMYK 300 DPI
2. Invoice US Letter – 8.5" x 11" CMYK 300 DPI
3. Fax Cover Sheet US Letter – 8.5" x 11" CMYK 300 DPI
4. Email Signature

Including: logo, motto, address with phone and fax numbers, web address, and compliance disclosure.

5. Standard Envelope #10 – 9,5” x 4,125” CMYK 300 Dpi
6. Large Envelope – 9” x 12” CMYK 300 Dpi

Including: logo, motto, addresses without phone and fax numbers, web address, and compliance disclosure.

7. Letterhead Follower US Letter – 8.5" x 11" CMYK 300 DPI

Including: logo, motto, and web address.

8. Flat Invitation Cards – 6” x 4” CMYK 300 Dpi
9. Pocket Folder – 9" x 12”, CMYK 300 Dpi

Including: logo and motto.

Here is the info:

Company: Harrowmere Wealth Management LLC
Address 1: 4715 Lantern Ave. Suite K-12, Willow Grove, PA, 19090
Phone 1: 1-215-555-0172
Address 2: 618 Fenwick Circle, New London Twp., PA, 19352
Phone 2: 1-610-555-0139
Fax: 1-484-555-0196
Motto: Steady Hands Since Day One (in grey #A8A8A8 and US Declaration font)
Web address: www.harrowmerewealth.example
Compliance disclosure: Securities and Advisory Services offered through QVR Capital. Member NASTO/CUDA.
Logo: in uploaded files

Industry/Entity Type

Business

Requirements
Must have
• Need to blend the business card look and feel with the brochure/website look and feel.

```html
<!DOCTYPE html>
<html lang="en">
<head>
<meta charset="utf-8">
<title>Harrowmere Wealth Management – Pocket Folder</title>
<link rel="stylesheet" href="https://fonts.googleapis.com/css2?family=Cormorant+Garamond:wght@500&family=Lato:wght@400&display=swap">
<style>
  :root {
    --stage: #dde3e7;
    --navy-light: #4b4d73;
    --navy: #34365b;
    --navy-deep: #27284a;
    --pocket: #2f3154;
    --paper-grey: #e7e8ea;
    --paper-grey-soft: #f1f1f2;
    --ink-white: #ffffff;
    --ink-muted: #a9abc4;
  }
  * { box-sizing: border-box; margin: 0; padding: 0; }
  html, body {
    width: 1200px; height: 857px; overflow: hidden;
    background: var(--stage);
  }
  .folder-set {
    position: absolute; left: 40px; top: 188px;
    display: flex; gap: 40px;
  }
  .panel {
    position: relative; width: 360px; height: 480px; overflow: hidden;
  }
  /* Front cover */
  .cover {
    background: linear-gradient(180deg, var(--navy-light) 0%, var(--navy) 45%, var(--navy-deep) 100%);
  }
  .cover-bands { position: absolute; inset: 0; }
  .brand {
    position: absolute; top: 70px; left: 0; right: 0;
    display: flex; flex-direction: column; align-items: center; gap: 12px;
    color: var(--ink-white);
  }
  .brand-mark { width: 14px; height: 14px; background: var(--ink-white); }
  .brand-name {
    font-family: "Cormorant Garamond", serif; font-weight: 500;
    font-size: 17px; letter-spacing: 2px; text-transform: uppercase;
    text-align: center; line-height: 1.3;
  }
  .web-address {
    position: absolute; left: 0; right: 0; bottom: 34px; text-align: center;
    font-family: "Lato", sans-serif; font-size: 9px; letter-spacing: 1px;
    color: var(--ink-muted);
  }
  /* Inside spread */
  .spread { display: flex; box-shadow: 0 0 0 1px rgba(0,0,0,0.04); }
  .inside-pattern {
    position: absolute; inset: 0;
    background: linear-gradient(180deg, var(--paper-grey-soft), var(--paper-grey));
  }
  .inside-right .pocket { position: absolute; left: 0; bottom: 0; width: 360px; height: 200px; }
  .spine { position: absolute; top: 0; bottom: 0; left: 360px; width: 1px; background: rgba(0,0,0,0.08); }
</style>
</head>
<body>
  <main class="folder-set">
    <section class="panel cover" aria-label="Folder front cover">
      <svg class="cover-bands" viewBox="0 0 360 480" aria-hidden="true">
        <polygon points="0,190 360,150 360,200 0,250" fill="#ffffff" opacity="0.05"/>
        <polygon points="0,250 360,200 360,270 0,290" fill="#ffffff" opacity="0.03"/>
      </svg>
      <div class="brand">
        <span class="brand-mark"></span>
        <p class="brand-name">Harrowmere<br>Wealth Management</p>
      </div>
      <p class="web-address">www.harrowmerewealth.example</p>
    </section>

    <section class="spread" aria-label="Folder inside spread">
      <div class="panel inside-left">
        <div class="inside-pattern" role="img" aria-label="Light grey repeating brand pattern on the inside of the folder"></div>
      </div>
      <div class="panel inside-right">
        <div class="inside-pattern" role="img" aria-label="Light grey repeating brand pattern on the inside of the folder"></div>
        <svg class="pocket" viewBox="0 0 360 200" aria-label="Document pocket">
          <defs>
            <linearGradient id="pocketShade" x1="0" y1="0" x2="0" y2="1">
              <stop offset="0" stop-color="#3d3f66"/>
              <stop offset="1" stop-color="#27284a"/>
            </linearGradient>
          </defs>
          <polygon points="0,30 120,30 170,70 360,0 360,200 0,200" fill="url(#pocketShade)"/>
          <polyline points="0,30 120,30 170,70 360,0" fill="none" stroke="#55577e" stroke-width="1"/>
        </svg>
      </div>
    </section>
  </main>
</body>
</html>
```